Corbel Crest Lighting - Commercial & Residential Landscape Lighting

Landscape Lighting Services & Design: Create a website for our landscape lighting company. We would like the design to be tailored around this description:
Illuminate with Confidence. Designed with Precision. Installed with Care.
Locally and veteran-owned, we take pride in transforming outdoor spaces through innovative lighting solutions tailored to your vision. From landscape and holiday lighting to permanent installations, our effortless process and expert design deliver breathtaking results and lasting curb appeal. Backed by a lifetime warranty and quarterly service options, our commitment to quality and customer satisfaction is unwavering. Try before you buy and experience your home in a whole new light with our complimentary demo kit — see the stunning effects before you decide.
- Also, add in this information as well; Outdoor Lighting not only beautifies spaces but also significantly enhances safety by illuminating your home or business. Beautifully lit entrances deter potential intruders, making your home a safer place for your loved ones. we also offer quarterly service plans to ensure lighting equipment continues to operate & illuminate effectively throughout the year. Also mention we provide free estimates and we are offering a 10% discount to military, veterans, and first responders.

Target Market(s)

Luxury market

Industry/Entity Type

Landscape Lighting - Residential & Commercial Lighting Services

Coding

Coded - Design and coding required

Number of Pages Required

2 page

Colors
00AB8E
00BBA5
67D7C9
C6EFE9
E9F9F6
59FF00
82FF00
B8FF75
E3FFCB
F4FFEA
FFC000
F8CF3A
FAE287
FDF2CF
FEFAEE

Requirements
Must have
• a lead generation button where people can submit their information for us to reach out to them and schedule their free estimate, homepage, about page, contact page, products and services page, user friendly, easy to navigate, and it also must be engaging and eye popping, as well as appealing to the luxury market. Please use colors; verdent green, dark green, ivory, and sunny yellow. Also, include an about page that references our story; Glen is retired Army and he opened a fitness studio in 2017 with his wife Rosalind. He has installed low voltage lighting in every home he lived in and for his friends and family over the years and decided to open his own business because he is passionate about beautifying outdoor landscapes and highlighting a properties full potential, not only in the day but at night as well all while providing safety and security for his clients. Having a deep respect for nature and landscaping, he wants to provide the same care and quality to each of his clients as he has in the fitness industry for decades. He believes small businesses are the back bone of America and he's excited to provide a service that is all to often neglected in the design of a home.
Nice to have
• I would like to have a clear intent and purpose, engaging web design, clear call to action, optimized for search engines, mobile friendy design, security measures, credibility indicators

```html
<!DOCTYPE html>
<html lang="en">
<head>
<meta charset="utf-8">
<title>Corbel Crest Lighting – Residential &amp; Commercial Landscape Lighting</title>
<link rel="stylesheet" href="https://fonts.googleapis.com/css2?family=DM+Sans:wght@400;500;700&family=Lato:wght@400;700&family=Poppins:wght@500;700&display=swap">
<style>
:root{
  --green:#1c9070;
  --green-dark:#16775c;
  --sun:#f7a823;
  --mint:#e0f5f2;
  --ink:#111;
  --body:#444;
  --white:#fff;
  --night:#000;
}
*{box-sizing:border-box;margin:0;padding:0}
html,body{width:1200px;height:4348px;overflow:hidden;background:var(--white);font-family:"Lato",sans-serif;color:var(--body)}
.page{position:relative;width:1200px;height:4348px;overflow:hidden}
.abs{position:absolute}
.accent{color:var(--sun)}
.btn{position:absolute;display:flex;align-items:center;justify-content:center;border-radius:20px;font-family:"Lato",sans-serif;font-size:15px;color:var(--white);text-decoration:none}
.btn-sun{background:var(--sun)}
.btn-green{background:var(--green)}
.photo{position:absolute}

/* header */
.topbar{left:413px;top:0;width:787px;height:42px;background:var(--green);clip-path:polygon(0 0,100% 0,100% 100%,26px 100%);display:flex;align-items:center;gap:0;color:var(--white);font-family:"DM Sans",sans-serif;font-size:13px}
.topbar span{position:absolute;display:flex;align-items:center;gap:8px}
.brand{left:110px;top:12px;font-family:"DM Sans",sans-serif;font-weight:500;font-size:26px;color:#9b1b24;line-height:1.05;width:200px}
.brand small{display:block;font-size:11px;letter-spacing:1.2px;color:#9b1b24;margin-top:3px}
.nav a{position:absolute;top:64px;font-family:"DM Sans",sans-serif;font-size:15px;color:var(--ink);text-decoration:none}
.nav a.active{color:var(--sun)}
.nav a.active::after{content:"";position:absolute;left:0;right:0;top:25px;height:3px;background:var(--sun)}

/* hero */
.hero{left:0;top:98px;width:1200px;height:600px;background:linear-gradient(180deg,#5a4a78 0%,#c27aa5 14%,#4c3a34 35%,#2c2520 65%,#3a4a2a 88%);}
.hero h1{position:absolute;left:0;width:1200px;top:125px;text-align:center;font-family:"Poppins",sans-serif;font-weight:700;font-size:58px;line-height:84px;color:var(--white)}
.dots{left:580px;top:593px;display:flex;gap:4px}
.dots i{width:9px;height:9px;border-radius:50%;background:var(--white)}
.dots i:nth-child(2){background:var(--green)}

/* section headings */
.h2{font-family:"DM Sans",sans-serif;font-weight:500;font-size:44px;line-height:56px;color:var(--ink)}
.copy{font-size:14px;line-height:29px;color:var(--body)}
.copy p+p{margin-top:7px}

/* arch photos */
.arch{border-radius:180px 180px 0 0}
.arch-frame{position:absolute;border:4px solid var(--sun);border-right:none;border-bottom:none;border-radius:190px 190px 0 0}

/* services */
.card{position:absolute;top:2085px;width:233px;height:376px;background:var(--white);box-shadow:0 6px 14px rgba(0,0,0,.16)}
.card .photo{left:0;top:0;width:233px;height:325px;border-radius:116px 116px 0 0}
.card h3{position:absolute;left:0;right:0;top:338px;text-align:center;font-family:"Lato",sans-serif;font-weight:700;font-size:16px;color:var(--ink)}

/* demo */
.demo{left:111px;top:2552px;width:978px;height:360px;background:var(--green);border-radius:180px}
.demo h2{color:var(--white)}
.demo .copy{color:var(--white)}

/* footer */
.footer{left:0;top:3941px;width:1200px;height:407px;background:var(--night)}
.foot-h{position:absolute;font-family:"DM Sans",sans-serif;font-weight:500;font-size:21px;color:var(--green)}
.foot-list{position:absolute;list-style:none;font-family:"DM Sans",sans-serif;font-size:15px;line-height:33px;color:var(--white)}
.contact-item{position:absolute;left:858px;display:flex;align-items:center;gap:14px;font-family:"DM Sans",sans-serif;font-size:15px;color:var(--white)}
.social{position:absolute;top:4193px;width:28px;height:28px;border-radius:50%;background:var(--white)}
</style>
</head>
<body>
<div class="page">

  <!-- header -->
  <div class="abs brand">CORBEL CREST<small>RESIDENTIAL &amp; COMMERCIAL LIGHTING</small></div>
  <div class="abs topbar">
    <span style="left:64px">
      <svg width="12" height="16" viewBox="0 0 12 16"><path d="M6 0a6 6 0 0 0-6 6c0 4.5 6 10 6 10s6-5.5 6-10a6 6 0 0 0-6-6zm0 8.5A2.5 2.5 0 1 1 6 3.5a2.5 2.5 0 0 1 0 5z" fill="#fff"/></svg>
      Lorm Ipsum,USA -437916</span>
    <span style="left:296px">
      <svg width="16" height="16" viewBox="0 0 24 24"><path d="M6.6 10.8a15.2 15.2 0 0 0 6.6 6.6l2.2-2.2a1 1 0 0 1 1-.25 11.4 11.4 0 0 0 3.6.57 1 1 0 0 1 1 1V20a1 1 0 0 1-1 1A17 17 0 0 1 3 4a1 1 0 0 1 1-1h3.5a1 1 0 0 1 1 1c0 1.25.2 2.45.57 3.57a1 1 0 0 1-.25 1z" fill="#fff"/></svg>
      888 888 88888</span>
    <span style="left:452px">
      <svg width="16" height="12" viewBox="0 0 16 12"><rect width="16" height="12" rx="2" fill="#fff"/><path d="M1 1l7 5 7-5" stroke="#1c9070" stroke-width="1.6" fill="none"/></svg>
      info@corbelcrestlighting.com</span>
  </div>
  <nav class="nav">
    <a class="active" style="left:457px">Home</a>
    <a style="left:532px">AboutUs</a>
    <a style="left:624px">Products</a>
    <a style="left:717px">Services</a>
  </nav>
  <svg class="abs" style="left:928px;top:58px" width="24" height="24" viewBox="0 0 24 24"><circle cx="10" cy="10" r="7.5" stroke="#888" stroke-width="1.6" fill="none"/><path d="M15.5 15.5L22 22" stroke="#888" stroke-width="1.6"/></svg>
  <a class="btn btn-sun" style="left:967px;top:53px;width:115px;height:35px">Contact Us</a>

  <!-- hero -->
  <div class="abs hero" role="img" aria-label="Modern farmhouse glowing with warm exterior lighting at dusk">
    <h1>Illuminate with Confidence.<br>Designed with Precision.<br>Installed with Care.</h1>
  </div>
  <a class="btn btn-sun" style="left:543px;top:481px;width:115px;height:34px">Get Started</a>
  <div class="abs dots"><i></i><i></i><i></i></div>
  <svg class="abs" style="left:0;top:560px" width="1200" height="140" viewBox="0 0 1200 140" preserveAspectRatio="none">
    <path d="M0 40 Q600 200 1200 20 L1200 140 L0 140Z" fill="#fff"/>
    <path d="M0 40 Q600 200 1200 20" stroke="#1c9070" stroke-width="6" fill="none"/>
  </svg>

  <!-- about -->
  <h2 class="abs h2" style="left:113px;top:752px">About <span class="accent">Us</span></h2>
  <div class="abs copy" style="left:113px;top:818px;width:450px">
    <p>Glen is retired Army and he opened a fitness studio in 2017 with his wife Rosalind. He has installed low voltage lighting in every home he lived in and for his friends and family over the years and decided to open his own business because he is passionate about beautifying outdoor landscapes and highlighting a properties full potential, not only in the day but at night as well all while providing safety and security for his clients.</p>
    <p>Having a deep respect for nature and landscaping, he wants to provide the same care and quality to each of his clients as he has in the fitness industry for decades. He believes small businesses are the back bone of America and he's excited to provide a service that is all to often neglected in the design of a home</p>
  </div>
  <a class="btn btn-green" style="left:110px;top:1197px;width:113px;height:35px">Read More</a>
  <div class="arch-frame" style="left:684px;top:763px;width:358px;height:456px"></div>
  <div class="photo arch" style="left:692px;top:773px;width:350px;height:446px;background:linear-gradient(180deg,#2c4b86 0%,#4a6aa0 35%,#4a3e34 60%,#7c7466 100%)" role="img" aria-label="Stone estate home with lit windows and a paved driveway at twilight"></div>

  <!-- distinction band -->
  <div class="abs" style="left:604px;top:1318px;width:596px;height:505px;background:var(--mint)"></div>
  <div class="photo" style="left:0;top:1318px;width:599px;height:505px;border-radius:0 240px 0 0;background:linear-gradient(180deg,#3a3c52 0%,#5b5a66 30%,#4a3a28 60%,#1d3a44 100%)" role="img" aria-label="Luxury resort-style home with a lit pool terrace at night"></div>
  <h2 class="abs h2" style="left:641px;top:1365px;width:480px">Breathtaking Outdoor Lighting, <span class="accent">Designed for Distinction</span></h2>
  <p class="abs copy" style="left:644px;top:1539px;width:460px;font-family:'DM Sans',sans-serif;font-size:13.5px;line-height:31px">Locally and veteran-owned, we take pride in transforming outdoor spaces through innovative lighting solutions tailored to your vision. From landscape and holiday lighting to permanent installations, our effortless process and expert design deliver breathtaking results and lasting curb appeal. Backed by a lifetime warranty and quarterly service options, our commitment to quality and customer satisfaction is unwavering</p>

  <!-- services -->
  <h2 class="abs h2" style="left:0;width:1200px;text-align:center;top:1900px">Our <span class="accent">Services</span></h2>
  <p class="abs copy" style="left:300px;width:600px;text-align:center;top:1973px;font-size:15px">More than just beautiful — our lighting solutions provide peace of mind, enhanced visibility, and added security for your home or business.</p>
  <div class="card" style="left:113px"><div class="photo" style="background:linear-gradient(180deg,#2d3320 0%,#5a5a2c 50%,#4d7a30 100%)" role="img" aria-label="Bollard path light among garden shrubs"></div><h3>Landscape Lighting</h3></div>
  <div class="card" style="left:361px"><div class="photo" style="background:linear-gradient(180deg,#2a3048 0%,#9aa0aa 45%,#6a4030 100%)" role="img" aria-label="House entrance dressed in holiday wreaths and lights"></div><h3>Holiday Lighting</h3></div>
  <div class="card" style="left:609px"><div class="photo" style="background:linear-gradient(180deg,#7a7e7a 0%,#2a2a2a 50%,#3a3a24 100%)" role="img" aria-label="Technician installing a garden spotlight"></div><h3>Permanent Installations</h3></div>
  <div class="card" style="left:857px"><div class="photo" style="background:linear-gradient(180deg,#6a4a30 0%,#b08a60 45%,#8a6a4a 100%)" role="img" aria-label="Wall-mounted security light on siding"></div><h3>Security &amp; Safety Lighting</h3></div>

  <!-- demo kit -->
  <div class="abs demo">
    <h2 class="abs h2" style="left:97px;top:58px;width:520px">Complimentary Demo Kit Available</h2>
    <p class="abs copy" style="left:97px;top:170px;width:420px;font-family:'DM Sans',sans-serif;font-size:14px;line-height:28px">&nbsp;Try before you buy and experience your home in a whole new light with our complimentary demo kit — see the stunning effects before you decide.</p>
    <a class="btn btn-sun" style="left:97px;top:274px;width:157px;height:34px;font-size:14px">Book Your Demo</a>
  </div>
  <div class="abs" style="left:738px;top:2568px;width:324px;height:324px;border-radius:50%;background:var(--white)"></div>
  <div class="photo" style="left:746px;top:2576px;width:308px;height:308px;border-radius:50%;background:linear-gradient(180deg,#6a7088 0%,#3a4030 40%,#8a6a3a 60%,#3e5a24 100%)" role="img" aria-label="Ranch home with warm landscape lighting across the lawn at dusk"></div>

  <!-- secure -->
  <div class="arch-frame" style="left:110px;top:3001px;width:359px;height:412px"></div>
  <div class="photo arch" style="left:118px;top:3013px;width:351px;height:400px;background:linear-gradient(180deg,#2a3a22 0%,#6a5a6a 35%,#8a8a80 65%,#4a7a2a 100%)" role="img" aria-label="Garden bed with river stones and small path lights"></div>
  <h2 class="abs h2" style="left:643px;top:3009px;width:460px;line-height:52px">Secure Your <span class="accent">Space with Style</span></h2>
  <p class="abs copy" style="left:647px;top:3132px;width:440px;font-size:13.5px">Outdoor Lighting not only beautifies spaces but also significantly enhances safety by illuminating your home or business. Beautifully lit entrances deter potential intruders, making your home a safer place for your loved ones. we also offer quarterly service plans to ensure lighting equipment continues to operate &amp; illuminate effectively throughout the year.</p>
  <a class="btn btn-green" style="left:645px;top:3330px;width:113px;height:35px">Read More</a>

  <!-- military discount -->
  <div class="photo" style="left:106px;top:3487px;width:976px;height:362px;border-radius:181px;background:linear-gradient(180deg,#1e2630 0%,#2c3036 40%,#4a3a30 75%,#1e2a1a 100%)" role="img" aria-label="Suburban home exterior lit at night among trees"></div>
  <h2 class="abs h2" style="left:106px;width:976px;text-align:center;top:3529px;color:var(--white);line-height:55px">Exclusive Discount for<br>Military &amp; First Responders</h2>
  <p class="abs" style="left:106px;width:976px;text-align:center;top:3652px;font-family:'DM Sans',sans-serif;font-size:21px;line-height:34px;color:var(--white)">we provide free estimates and we are offering a<br><span class="accent" style="font-weight:700;font-size:31px">10%</span> discount to military, veterans, and first responders.</p>
  <a class="btn btn-sun" style="left:493px;top:3762px;width:216px;height:34px;font-size:14px">Schedule Your &nbsp;free Estimate</a>

  <!-- footer -->
  <svg class="abs" style="left:0;top:3925px" width="1200" height="80" viewBox="0 0 1200 80" preserveAspectRatio="none">
    <path d="M0 60 Q600 -30 1200 60 L1200 80 L0 80Z" fill="#000"/>
    <path d="M0 60 Q600 -30 1200 60" stroke="#1c9070" stroke-width="6" fill="none"/>
  </svg>
  <div class="abs footer"></div>
  <div class="abs" style="left:110px;top:4055px;font-family:'DM Sans',sans-serif;font-weight:500;font-size:38px;line-height:44px;color:var(--sun);width:260px">CORBEL CREST<div style="font-size:15px;letter-spacing:2.4px;line-height:24px">LIGHTING</div></div>
  <div class="social" style="left:114px"></div>
  <div class="social" style="left:149px"></div>
  <div class="social" style="left:184px"></div>
  <div class="social" style="left:219px"></div>
  <div class="social" style="left:254px"></div>

  <div class="foot-h" style="left:466px;top:4057px">Quick Links</div>
  <ul class="foot-list" style="left:469px;top:4097px"><li>Home</li><li>About Us</li><li>Services</li><li>Products</li><li>Contact Us</li></ul>
  <div class="foot-h" style="left:628px;top:4057px">Other Links</div>
  <ul class="foot-list" style="left:632px;top:4097px"><li>Privacy Policy</li><li>Terms &amp; Conditions</li><li>Disclaimer</li><li>FAQ's</li><li>Support</li><li>Help</li></ul>
  <div class="foot-h" style="left:856px;top:4057px">Contact Info</div>
  <div class="contact-item" style="top:4103px"><svg width="22" height="22" viewBox="0 0 24 24"><circle cx="12" cy="12" r="11" fill="#fff"/><path d="M12 5a4.5 4.5 0 0 0-4.5 4.5c0 3.4 4.5 8.5 4.5 8.5s4.5-5.1 4.5-8.5A4.5 4.5 0 0 0 12 5zm0 6.3a1.8 1.8 0 1 1 0-3.6 1.8 1.8 0 0 1 0 3.6z" fill="#000"/></svg>Lorem Ipsum, USA -437916</div>
  <div class="contact-item" style="top:4159px"><svg width="22" height="22" viewBox="0 0 24 24"><circle cx="12" cy="12" r="11" fill="#fff"/><path d="M9 7.5l1.6 2.6-1 1.2a7 7 0 0 0 3.1 3.1l1.2-1L16.5 15l-.6 1.8c-4.6-.3-8.4-4.1-8.7-8.7z" fill="#000"/></svg>+1 888 888 8888</div>
  <div class="contact-item" style="top:4213px"><svg width="22" height="22" viewBox="0 0 24 24"><circle cx="12" cy="12" r="11" fill="#fff"/><rect x="6" y="8" width="12" height="8" rx="1" fill="#000"/><path d="M6.5 8.5L12 12.5l5.5-4" stroke="#fff" stroke-width="1.2" fill="none"/></svg>info@corbelcrestlighting.com</div>

  <div class="abs" style="left:110px;top:4311px;width:980px;height:1px;background:#555"></div>
  <p class="abs" style="left:0;width:1200px;text-align:center;top:4322px;font-family:'DM Sans',sans-serif;font-size:14px;color:var(--white)">© 2025 Corbel Crest Lighting.All rights reserved</p>
</div>
</body>
</html>
```